Halvern Power "Unique Process" Graphic

Create a "graphic" that creatively represents the seven-step process that Halvern Power uses to serve our customers.
This graphic should be sized in such a way that it can easily be included on a page in our website, and also used in other marketing materials such as flyers, emails and powerpoint presentations.
As an EXAMPLE of a similar graphic, see the "Proven Process" section of the home page of this website - https://www.trelvonsite.com/
I'll include our brand documentation as well as the document for our "Unique Process" in the uploaded files section.
Please use our brand colors and also be creative in how you represent the seven steps graphically.
Here's a bit about our business.
Halvern Power is one of the largest B2B Energy Brokers in the US. We serve tens of thousands of customers by securing energy contracts for them. We are NOT an energy company ourselves - but a broker that represents 30+ energy suppliers to commercial and nonprofit customers.

```html
<!DOCTYPE html>
<html lang="en">
<head>
<meta charset="utf-8">
<title>Halvern Power – Unique Process</title>
<link href="https://fonts.googleapis.com/css2?family=Lato:wght@400;700;900&display=swap" rel="stylesheet">
<style>
  :root {
    --green: #00963a;
    --green-dark: #006e2a;
    --navy: #052c6b;
    --navy-dark: #021d4a;
    --tile: #bdbdbd;
    --icon-green: #1e4a36;
    --icon-navy: #0b2350;
    --number: #2f2f2f;
    --white: #ffffff;
  }
  html, body { margin: 0; padding: 0; overflow: hidden; background: var(--white); }
  .canvas { width: 960px; height: 1200px; position: relative; overflow: hidden; }
  .process { display: block; font-family: "Lato", sans-serif; }
  .step-label { font-weight: 700; font-size: 18px; fill: var(--white); text-anchor: middle; }
  .step-number { font-weight: 700; font-size: 30px; fill: var(--number); text-anchor: middle; }
  .step-title { font-size: 12px; fill: var(--white); letter-spacing: 0.6px; }
  .step-title .brand { font-weight: 900; }
  .step-body { font-size: 8px; fill: var(--white); letter-spacing: 0.2px; }
  .accent-green { fill: #1fd15c; font-weight: 900; }
  .accent-navy { fill: var(--navy); font-weight: 900; }
  .icon { fill: none; stroke-width: 2; stroke-linecap: round; stroke-linejoin: round; }
  .icon-green { stroke: var(--icon-green); }
  .icon-navy { stroke: var(--icon-navy); }
  .connector { stroke-width: 4; stroke-linecap: butt; }
</style>
</head>
<body>
<div class="canvas">
<svg class="process" width="960" height="1200" viewBox="0 0 960 1200" xmlns="http://www.w3.org/2000/svg">
  <defs>
    <radialGradient id="disc" cx="40%" cy="35%" r="75%">
      <stop offset="0" stop-color="#ffffff"/>
      <stop offset="0.6" stop-color="#f1f1f1"/>
      <stop offset="1" stop-color="#cfcfcf"/>
    </radialGradient>
    <linearGradient id="numberFace" x1="0" y1="0" x2="0" y2="1">
      <stop offset="0" stop-color="#f4f4f4"/>
      <stop offset="1" stop-color="#c9c9c9"/>
    </linearGradient>
    <clipPath id="innerClip"><circle r="36"/></clipPath>
  </defs>

  <!-- connectors -->
  <g class="connectors">
    <line class="connector" x1="462" y1="246" x2="480" y2="270" stroke="var(--green)"/>
    <line class="connector" x1="480" y1="270" x2="498" y2="294" stroke="var(--navy)"/>
    <line class="connector" x1="498" y1="378" x2="480" y2="402" stroke="var(--navy)"/>
    <line class="connector" x1="480" y1="402" x2="462" y2="426" stroke="var(--green)"/>
    <line class="connector" x1="462" y1="510" x2="480" y2="534" stroke="var(--green)"/>
    <line class="connector" x1="480" y1="534" x2="498" y2="558" stroke="var(--navy)"/>
    <line class="connector" x1="498" y1="642" x2="480" y2="666" stroke="var(--navy)"/>
    <line class="connector" x1="480" y1="666" x2="462" y2="690" stroke="var(--green)"/>
    <line class="connector" x1="462" y1="774" x2="480" y2="798" stroke="var(--green)"/>
    <line class="connector" x1="480" y1="798" x2="498" y2="822" stroke="var(--navy)"/>
    <line class="connector" x1="498" y1="906" x2="480" y2="930" stroke="var(--navy)"/>
    <line class="connector" x1="480" y1="930" x2="462" y2="954" stroke="var(--green)"/>
  </g>

  <!-- Step 01 -->
  <g class="step step-right">
    <rect x="420" y="165.6" width="318" height="76.8" fill="var(--green)"/>
    <rect x="738" y="165.6" width="77" height="76.8" fill="var(--tile)"/>
    <text class="step-title" x="484" y="188"><tspan class="brand">HALVERN</tspan> ASSESSMENT</text>
    <text class="step-body" x="485" y="205">Spend 15 minutes with our team while we analyze your</text>
    <text class="step-body" x="485" y="215">account and contract details to select suppliers that fit</text>
    <text class="step-body" x="485" y="225">your needs.</text>
    <g class="icon icon-green" transform="translate(776,204)">
      <rect x="-14" y="-16" width="24" height="30" rx="2"/>
      <rect x="-6" y="-20" width="8" height="5" rx="1"/>
      <path d="M-10 -8 l2 2 l3 -3 M-3 -7 h8 M-10 0 l2 2 l3 -3 M-3 1 h8"/>
      <circle cx="11" cy="11" r="7"/>
      <path d="M11 8 v3 h3"/>
      <circle cx="-20" cy="-10" r="1.5"/><circle cx="17" cy="-18" r="2"/><circle cx="-21" cy="17" r="2"/>
    </g>
    <g transform="translate(420,204)">
      <circle r="58" fill="url(#disc)" stroke="var(--green)" stroke-width="5"/>
      <circle cx="4" cy="2" r="42" fill="var(--green-dark)"/>
      <circle r="41" fill="var(--green)"/>
      <rect x="-36" y="-3" width="72" height="40" fill="url(#numberFace)" clip-path="url(#innerClip)"/>
      <text class="step-label" y="-9">STEP</text>
      <text class="step-number" y="24">01</text>
    </g>
  </g>

  <!-- Step 02 -->
  <g class="step step-left">
    <rect x="222" y="297.6" width="318" height="76.8" fill="var(--navy)"/>
    <rect x="145" y="297.6" width="77" height="76.8" fill="var(--tile)"/>
    <text class="step-title" x="244" y="320"><tspan class="brand">HALVERN</tspan> OPTION!</text>
    <text class="step-body" x="244" y="335">We’ll send you an energy quote with at least three options</text>
    <text class="step-body" x="244" y="345">to choose from - including different suppliers and contract</text>
    <text class="step-body" x="244" y="355">terms. Our unbiased advice will help you find the best</text>
    <text class="step-body" x="244" y="365">solution!</text>
    <g class="icon icon-navy" transform="translate(183,338)">
      <rect x="-19" y="-16" width="38" height="34" rx="2"/>
      <path d="M-19 -9 h38"/>
      <rect x="-13" y="-4" width="26" height="9"/>
      <path d="M0 2 v12 a5 5 0 0 0 10 0 v-5"/>
      <circle cx="-21" cy="-22" r="1.5"/><circle cx="14" cy="-23" r="2"/>
    </g>
    <g transform="translate(540,336)">
      <circle r="58" fill="url(#disc)" stroke="var(--navy)" stroke-width="5"/>
      <circle cx="-4" cy="2" r="42" fill="var(--navy-dark)"/>
      <circle r="41" fill="var(--navy)"/>
      <rect x="-36" y="-3" width="72" height="40" fill="url(#numberFace)" clip-path="url(#innerClip)"/>
      <text class="step-label" y="-9">STEP</text>
      <text class="step-number" y="24">02</text>
    </g>
  </g>

  <!-- Step 03 -->
  <g class="step step-right">
    <rect x="420" y="429.6" width="318" height="76.8" fill="var(--green)"/>
    <rect x="738" y="429.6" width="77" height="76.8" fill="var(--tile)"/>
    <text class="step-title" x="484" y="452"><tspan class="brand">HALVERN</tspan> SIGN-UP!</text>
    <text class="step-body" x="485" y="469">Our simple sign-up process is handled electronically. Even</text>
    <text class="step-body" x="485" y="479">contract signatures.</text>
    <g class="icon icon-green" transform="translate(776,468)">
      <rect x="-18" y="-16" width="26" height="34" rx="1"/>
      <path d="M-14 -16 v-3 h26 v34 h-4 M12 -19 v-3 h4 v34 h-4"/>
      <circle cx="-10" cy="-8" r="3"/>
      <path d="M-15 0 a5 5 0 0 1 10 0 M-15 6 h20 M-15 10 h20 M-15 14 h20 M-1 -8 h6"/>
    </g>
    <g transform="translate(420,468)">
      <circle r="58" fill="url(#disc)" stroke="var(--green)" stroke-width="5"/>
      <circle cx="4" cy="2" r="42" fill="var(--green-dark)"/>
      <circle r="41" fill="var(--green)"/>
      <rect x="-36" y="-3" width="72" height="40" fill="url(#numberFace)" clip-path="url(#innerClip)"/>
      <text class="step-label" y="-9">STEP</text>
      <text class="step-number" y="24">03</text>
    </g>
  </g>

  <!-- Step 04 -->
  <g class="step step-left">
    <rect x="222" y="561.6" width="318" height="76.8" fill="var(--navy)"/>
    <rect x="145" y="561.6" width="77" height="76.8" fill="var(--tile)"/>
    <text class="step-title" x="244" y="584"><tspan class="brand">HALVERN</tspan> QA</text>
    <text class="step-body" x="244" y="599">Every order detail is confirmed to ensure accuracy and</text>
    <text class="step-body" x="244" y="609">smooth processing.</text>
    <g class="icon icon-navy" transform="translate(183,600)">
      <path d="M-2 -14 a12 11 0 1 1 16 14 l3 4 l-7 -2"/>
      <circle cx="-4" cy="2" r="13"/>
      <path d="M-12 18 l3 -5 M-10 -2 h12 M-10 2 h12 M-10 6 h12"/>
      <circle cx="-20" cy="-16" r="2"/><circle cx="16" cy="16" r="1.5"/>
    </g>
    <g transform="translate(540,600)">
      <circle r="58" fill="url(#disc)" stroke="var(--navy)" stroke-width="5"/>
      <circle cx="-4" cy="2" r="42" fill="var(--navy-dark)"/>
      <circle r="41" fill="var(--navy)"/>
      <rect x="-36" y="-3" width="72" height="40" fill="url(#numberFace)" clip-path="url(#innerClip)"/>
      <text class="step-label" y="-9">STEP</text>
      <text class="step-number" y="24">04</text>
    </g>
  </g>

  <!-- Step 05 -->
  <g class="step step-right">
    <rect x="420" y="693.6" width="318" height="76.8" fill="var(--green)"/>
    <rect x="738" y="693.6" width="77" height="76.8" fill="var(--tile)"/>
    <text class="step-title" x="484" y="716"><tspan class="brand">HALVERN</tspan> MONITORING</text>
    <text class="step-body" x="485" y="733">We proactively monitor your accounts to address any</text>
    <text class="step-body" x="485" y="743">contractual issues with suppliers, should they arise.</text>
    <text class="step-body" x="485" y="753">(E.g., You sell your business, account number changes, etc.)</text>
    <g class="icon icon-green" transform="translate(776,732)">
      <circle cx="-6" cy="-6" r="14"/>
      <path d="M-16 -6 q10 -9 20 0 q-10 9 -20 0"/>
      <circle cx="-6" cy="-6" r="2.5"/>
      <path d="M4 5 l12 12 M-20 18 h40 M16 -18 v12"/>
    </g>
    <g transform="translate(420,732)">
      <circle r="58" fill="url(#disc)" stroke="var(--green)" stroke-width="5"/>
      <circle cx="4" cy="2" r="42" fill="var(--green-dark)"/>
      <circle r="41" fill="var(--green)"/>
      <rect x="-36" y="-3" width="72" height="40" fill="url(#numberFace)" clip-path="url(#innerClip)"/>
      <text class="step-label" y="-9">STEP</text>
      <text class="step-number" y="24">05</text>
    </g>
  </g>

  <!-- Step 06 -->
  <g class="step step-left">
    <rect x="222" y="825.6" width="318" height="76.8" fill="var(--navy)"/>
    <rect x="145" y="825.6" width="77" height="76.8" fill="var(--tile)"/>
    <text class="step-title" x="244" y="848"><tspan class="brand">HALVERN</tspan> RENEWAL</text>
    <text class="step-body" x="244" y="863">To protect your business from market volatility, we</text>
    <text class="step-body" x="244" y="873">contact you ahead of your contract end date to discuss</text>
    <text class="step-body" x="244" y="883">renewal options. If anyone else contacts you, you respond,</text>
    <text class="step-body" x="244" y="893">“No thank you, <tspan class="accent-green">we have Halvern!</tspan>”</text>
    <g class="icon icon-navy" transform="translate(183,864)">
      <path d="M-14 -20 h26 a4 4 0 0 1 0 8 h-4 v28 a4 4 0 0 1 -4 4 h-22 a4 4 0 0 1 0 -8 h4 z"/>
      <path d="M-8 -12 h14 M-8 -7 h14 M-8 -2 h14"/>
      <circle cx="-1" cy="9" r="5"/>
      <path d="M-1 6 v6"/>
    </g>
    <g transform="translate(540,864)">
      <circle r="58" fill="url(#disc)" stroke="var(--navy)" stroke-width="5"/>
      <circle cx="-4" cy="2" r="42" fill="var(--navy-dark)"/>
      <circle r="41" fill="var(--navy)"/>
      <rect x="-36" y="-3" width="72" height="40" fill="url(#numberFace)" clip-path="url(#innerClip)"/>
      <text class="step-label" y="-9">STEP</text>
      <text class="step-number" y="24">06</text>
    </g>
  </g>

  <!-- Step 07 -->
  <g class="step step-right">
    <rect x="420" y="957.6" width="318" height="76.8" fill="var(--green)"/>
    <rect x="738" y="957.6" width="77" height="76.8" fill="var(--tile)"/>
    <text class="step-title" x="484" y="980"><tspan class="brand">HALVERN</tspan> GUARANTEE</text>
    <text class="step-body" x="485" y="997">Sleep Easy! You’ll never fall “out of contract” with</text>
    <text class="step-body" x="485" y="1007"><tspan class="accent-navy">Halvern Power</tspan> as your broker.</text>
    <g class="icon icon-green" transform="translate(776,994)">
      <circle cx="0" cy="-6" r="16"/>
      <circle cx="0" cy="-6" r="9"/>
      <path d="M-8 8 l-5 12 l6 -3 l4 5 l3 -10 M8 8 l5 12 l-6 -3 l-4 5 l-3 -10"/>
      <circle cx="-18" cy="14" r="2"/><circle cx="19" cy="15" r="2"/>
    </g>
    <g transform="translate(420,996)">
      <circle r="58" fill="url(#disc)" stroke="var(--green)" stroke-width="5"/>
      <circle cx="4" cy="2" r="42" fill="var(--green-dark)"/>
      <circle r="41" fill="var(--green)"/>
      <rect x="-36" y="-3" width="72" height="40" fill="url(#numberFace)" clip-path="url(#innerClip)"/>
      <text class="step-label" y="-9">STEP</text>
      <text class="step-number" y="24">07</text>
    </g>
  </g>
</svg>
</div>
</body>
</html>
```